Brinewardsea.com Website design needed!!

We are looking for a website layout to match the attached logo. We specialize in Dive Charters and currently are located in the Virgin Islands off of St. Thomas. Please create a design that is compatible with Bootstrap and have the grid in mind. WE are looking for creative and extremely professional layout design.

Target Market(s)

Scuba Diving, Divers looking for a diving charter in the Virgin Islands.

Number of Pages Required

3 page

Font styles to use
Serif

Requirements
Must have
• Must be Bootstrap friendly.
• Must work with the logo we provided. Colors etc.

```html
<!DOCTYPE html>
<html lang="en">
<head>
<meta charset="utf-8">
<title>Brinewardsea — Dive Charters St. Thomas</title>
<link rel="stylesheet" href="https://fonts.googleapis.com/css2?family=Roboto:wght@400;500;700&family=Oswald:wght@500&family=Pacifico&display=swap">
<style>
:root{
  --navy:#262f72;
  --navy-deep:#1e2560;
  --red:#e3222f;
  --blue:#1f7fd8;
  --yellow:#ffd630;
  --ink:#222;
  --muted:#666;
  --white:#fff;
  --line:#ddd;
}
*{box-sizing:border-box;margin:0;padding:0}
html,body{width:688px;height:1200px;overflow:hidden;background:var(--white)}
body{position:relative;font-family:"Roboto",Arial,sans-serif;color:var(--ink)}
.abs{position:absolute}
.script{font-family:"Pacifico",cursive;font-weight:400}

/* header */
.site-header{left:0;top:0;width:688px;height:52px;background:var(--white)}
.brand{left:92px;top:14px;display:flex;align-items:center;gap:6px}
.brand-dot{width:18px;height:18px;border-radius:50%;background:var(--blue)}
.brand-name{font-weight:700;font-size:15px;color:var(--red)}
.main-nav{left:266px;top:0;height:52px;display:flex}
.main-nav a{display:flex;align-items:center;padding:0 11px;font-size:8.5px;color:var(--ink);text-decoration:none;border-left:1px solid #eee;position:relative}
.main-nav a.active{color:var(--red)}
.main-nav a.active::after{content:"";position:absolute;left:11px;right:11px;top:32px;height:2px;background:var(--red)}
.header-phone{left:500px;top:12px;display:flex;gap:5px;align-items:flex-start}
.header-phone small{display:block;font-size:8px;color:#555;letter-spacing:.3px}
.header-phone strong{display:block;font-size:12.5px;color:var(--red);font-weight:700}

/* hero */
.hero{left:0;top:52px;width:688px;height:278px;background:linear-gradient(160deg,#0b5fb8 0%,#1380d0 40%,#0e5d9f 75%,#6a8c92 100%)}
.hero-arrow{top:160px}
.hero-kicker{left:0;width:688px;top:191px;text-align:center;color:var(--white);font-size:11px;letter-spacing:4px;font-weight:500}
.hero-title{left:0;width:688px;top:190px;text-align:center;color:var(--white);font-size:44px;line-height:70px}

/* search */
.search-tab{left:190px;top:283px;width:292px;height:22px;background:var(--navy);border-radius:10px 10px 0 0;color:var(--white);font-size:9.5px;font-weight:700;letter-spacing:1px;text-align:center;line-height:22px}
.search-bar{left:92px;top:303px;width:504px;height:45px;background:var(--navy);border-radius:0 0 12px 12px}
.radio-group{left:105px;top:314px;font-size:7px;color:var(--white)}
.radio-group label{display:flex;align-items:center;gap:4px;margin-bottom:5px}
.radio-group span{width:7px;height:7px;border-radius:50%;background:var(--blue);border:1.5px solid var(--white)}
.field{top:316px;height:19px;background:var(--white);border-radius:2px;font-size:7px;color:#777;padding:0 4px;display:flex;align-items:center;justify-content:space-between}
.field i{width:8px;height:7px;background:#999;border-radius:1px}
.search-btn{left:518px;top:316px;width:64px;height:19px;background:var(--red);color:var(--white);font-size:8px;font-weight:700;text-align:center;line-height:19px;border-radius:2px}

/* intro */
.intro-title{left:0;width:688px;top:372px;text-align:center;font-size:14.5px;font-weight:700;color:#222}
.intro-title .script{color:var(--red);font-size:14px}
.intro-copy{left:104px;width:480px;top:402px;text-align:center;font-size:6.3px;line-height:12px;color:var(--muted)}

/* program tiles */
.tile{top:446px;width:116px;height:120px;display:flex;align-items:center;justify-content:center;text-align:center}
.tile-label{font-family:"Oswald",sans-serif;font-weight:500;color:var(--white);font-size:15.5px;line-height:22px;text-transform:uppercase;padding-bottom:5px;border-bottom:1px solid rgba(255,255,255,.85)}

/* news */
.news-band{left:0;top:592px;width:688px;height:193px;background:linear-gradient(120deg,#1c2433,#0c1220 55%,#2a1c1e)}
.news-card{left:92px;top:617px;width:154px;height:142px;background:var(--white);padding:10px 10px 0 13px}
.news-card h2{color:var(--red);font-size:15px;line-height:22px}
.news-card p{font-size:6.1px;line-height:12px;color:var(--muted);margin-top:4px}
.pager{display:flex;gap:4px;margin-top:6px}
.pager span{width:13px;height:13px;display:flex;align-items:center;justify-content:center}
.story{top:617px;width:104px;height:142px}
.story-img{width:104px;height:104px}
.story-caption{height:38px;background:var(--white);display:flex;justify-content:space-between}
.story-caption p{font-size:7.5px;font-weight:500;line-height:12px;padding:8px 0 0 9px}
.story-caption span{width:11px;display:flex;align-items:center;justify-content:center}

/* media */
.media-title{top:806px;color:var(--red);font-size:15px}
.media-sub{top:833px;font-size:6.5px;color:#333}
.media{top:853px;width:246px;height:147px}

/* cta */
.cta-help{left:0;top:1026px;width:344px;height:86px;background:linear-gradient(90deg,#1668c8,#1f86e0);color:var(--white)}
.cta-flex{left:344px;top:1026px;width:344px;height:86px;background:linear-gradient(90deg,#d81f3a,#e0263c)}
.cta-inner{position:absolute;top:0;width:200px;text-align:center}
.cta-help .cta-inner{left:118px}
.cta-flex .cta-inner{left:26px}
.cta-help h3,.cta-flex h3{color:var(--yellow);font-size:14px;line-height:20px;font-weight:400}
.cta-help h3{margin-top:9px}
.cta-help p{font-size:7.5px;line-height:11px}
.cta-help strong{display:block;font-size:15px;font-weight:400;line-height:18px;margin-top:2px}
.cta-help small{display:block;font-size:6.5px;margin-top:1px}
.cta-flex h3{margin-top:9px}
.cta-btn{display:inline-block;margin-top:4px;background:var(--white);color:#222;font-size:7.5px;font-weight:500;width:72px;height:20px;line-height:20px}

/* footer */
.site-footer{left:0;top:1112px;width:688px;height:88px;background:var(--navy)}
.social{left:296px;top:1131px;display:flex;gap:6px}
.social span{width:20px;height:20px;border-radius:50%;border:1.5px solid var(--white)}
.footer-nav{left:0;width:688px;top:1162px;text-align:center;font-size:7px;color:var(--white);word-spacing:2px}
.footer-nav b{font-weight:400;margin:0 9px}
.copyright{left:0;width:688px;top:1175px;text-align:center;font-size:6px;color:#d0d4ee}
</style>
</head>
<body>

<header class="site-header abs">
  <div class="brand abs"><span class="brand-dot"></span><span class="brand-name">Brinewardsea</span></div>
  <nav class="main-nav abs">
    <a class="active" href="#">HOME</a><a href="#">ABOUT US</a><a href="#">CONTACT</a><a href="#">SCHEDULE</a>
  </nav>
  <div class="header-phone abs">
    <svg width="12" height="12" viewBox="0 0 24 24" style="margin-top:12px"><path fill="#bbb" d="M6.6 10.8a15 15 0 0 0 6.6 6.6l2.2-2.2c.3-.3.7-.4 1-.2 1.1.4 2.3.6 3.6.6.6 0 1 .4 1 1V20c0 .6-.4 1-1 1A17 17 0 0 1 3 4c0-.6.4-1 1-1h3.5c.6 0 1 .4 1 1 0 1.3.2 2.5.6 3.6.1.3 0 .7-.2 1z"/></svg>
    <div><small>FOR MORE DETAILS</small><strong>(844)-555-0192</strong></div>
  </div>
</header>

<section class="hero abs" role="img" aria-label="Photo of a scuba diver swimming over a colourful coral reef"></section>
<svg class="hero-arrow abs" style="left:92px" width="10" height="16" viewBox="0 0 10 16"><path d="M8 1 2 8l6 7" stroke="#fff" stroke-width="1.5" fill="none"/></svg>
<svg class="hero-arrow abs" style="left:586px" width="10" height="16" viewBox="0 0 10 16"><path d="M2 1l6 7-6 7" stroke="#fff" stroke-width="1.5" fill="none"/></svg>
<p class="hero-kicker abs">THE BRINEWARDSEA</p>
<h1 class="hero-title abs script">Experience</h1>

<div class="search-tab abs">SEARCH FOR YOUR DREAM CHARTER TODAY!</div>
<form class="search-bar abs"></form>
<div class="radio-group abs">
  <label><span></span>I have approximate dates</label>
  <label><span style="border-color:var(--blue)"></span>I'm flexible</label>
</div>
<div class="field abs" style="left:196px;width:55px">From<i></i></div>
<div class="field abs" style="left:260px;width:54px">To<i></i></div>
<div class="field abs" style="left:322px;width:90px">First Name<i></i></div>
<div class="field abs" style="left:420px;width:90px">Email<i></i></div>
<div class="search-btn abs">SEARCH</div>

<h2 class="intro-title abs">THE BRAND NEW SCUBA DIVING PLATFORM : <span class="script">Brinewardsea</span></h2>
<p class="intro-copy abs">Lorem ipsum dolor sit amet, consectetur adipiscing elit, sed do eiusmod tempor incididunt ut labore et dolore magna aliqua. Ut enim ad minim veniam, quis nostrud exercitation ullamco laboris nisi ut aliquip ex ea commodo consequat. Duis aute irure dolor in reprehenderit in voluptate velit esse cillum dolore eu fugiat nulla pariatur. Excepteur sint occaecat cupidatat non proident, sunt in culpa qui officia deserunt mollit anim id est laborum.</p>

<div class="tile abs" style="left:92px;background:linear-gradient(160deg,#2b8fa8,#0f5a6e)" role="img" aria-label="Photo of two divers underwater"><span class="tile-label">Sailing<br>Program</span></div>
<div class="tile abs" style="left:221px;background:linear-gradient(160deg,#1d66c8,#0b2f8a)" role="img" aria-label="Photo of a group of scuba divers"><span class="tile-label">Scuba<br>Diving</span></div>
<div class="tile abs" style="left:350px;background:linear-gradient(160deg,#1b5a9a,#123a5e)" role="img" aria-label="Photo of a diver beside a sea turtle"><span class="tile-label">Marine<br>Biology</span></div>
<div class="tile abs" style="left:479px;background:linear-gradient(160deg,#1670d0,#0a3c96)" role="img" aria-label="Photo of a diver among orange reef fish"><span class="tile-label">Community<br>Service</span></div>

<section class="news-band abs" role="img" aria-label="Dark photo of a coral reef"></section>
<article class="news-card abs">
  <h2 class="script">Latest News</h2>
  <p>Sed ut perspiciatis unde omnis iste natus error sit voluptatem accusantium doloremque laudantium, totam rem aperiam, eaque ipsa quae ab illo inventore veritatis et quasi architecto beatae vitae dicta sunt explicabo. Nemo enim ipsam voluptatem</p>
  <div class="pager">
    <span style="background:var(--navy)"><svg width="6" height="8"><path d="M5 1 1 4l4 3" stroke="#fff" fill="none" stroke-width="1.3"/></svg></span>
    <span style="background:var(--red)"><svg width="6" height="8"><path d="M1 1l4 3-4 3" stroke="#fff" fill="none" stroke-width="1.3"/></svg></span>
  </div>
</article>
<article class="story abs" style="left:259px">
  <div class="story-img" style="background:linear-gradient(160deg,#1d74d8,#0c3e9a)" role="img" aria-label="Photo of two divers giving a sign underwater"></div>
  <div class="story-caption"><p>At vero eos et<br>accusamus et iusto</p><span style="background:var(--red)"><svg width="5" height="8"><path d="M1 1l3 3-3 3" stroke="#fff" fill="none" stroke-width="1.2"/></svg></span></div>
</article>
<article class="story abs" style="left:375px">
  <div class="story-img" style="background:linear-gradient(180deg,#8fc3ea,#d8d0c4 60%,#a55c4a)" role="img" aria-label="Photo of a family on a yacht deck"></div>
  <div class="story-caption"><p>Caribbean Luxury<br>Yacht Charter</p><span style="background:var(--blue)"><svg width="5" height="8"><path d="M1 1l3 3-3 3" stroke="#fff" fill="none" stroke-width="1.2"/></svg></span></div>
</article>
<article class="story abs" style="left:491px">
  <div class="story-img" style="background:linear-gradient(160deg,#2fb2e6,#0b3f86)" role="img" aria-label="Photo of three divers posing underwater"></div>
  <div class="story-caption"><p>Caribbean Luxury<br>Yacht Charter</p><span style="background:var(--blue)"><svg width="5" height="8"><path d="M1 1l3 3-3 3" stroke="#fff" fill="none" stroke-width="1.2"/></svg></span></div>
</article>

<h2 class="media-title abs script" style="left:92px">Video of the day</h2>
<p class="media-sub abs" style="left:92px">Lorem ipsum dolor sit amet</p>
<div class="media abs" style="left:92px;background:linear-gradient(160deg,#1e6d9a,#0c2f4a)" role="img" aria-label="Video still of a diver underwater">
  <svg class="abs" style="left:109px;top:60px" width="28" height="28" viewBox="0 0 28 28"><circle cx="14" cy="14" r="14" fill="#fff"/><path d="M11 8l9 6-9 6z" fill="#222"/></svg>
</div>
<h2 class="media-title abs script" style="left:350px">Photo of the day</h2>
<p class="media-sub abs" style="left:350px">Lorem ipsum dolor sit amet</p>
<div class="media abs" style="left:350px;width:245px;background:linear-gradient(160deg,#1a7fc8,#0d4c8c 60%,#3a6e6a)" role="img" aria-label="Photo of a diver beside a green sea turtle"></div>

<section class="cta-help abs">
  <div class="cta-inner">
    <h3 class="script">Have a Question?</h3>
    <p>We Are Here To Help!</p>
    <strong>(844)-555-0192</strong>
    <small>info@brinewardsea.com</small>
  </div>
</section>
<section class="cta-flex abs">
  <div class="cta-inner">
    <h3 class="script">We offer total flexibility<br>with our schedules.</h3>
    <a class="cta-btn">SCHEDULE</a>
  </div>
</section>

<footer class="site-footer abs"></footer>
<div class="social abs"><span></span><span></span><span></span><span></span></div>
<nav class="footer-nav abs">HOME<b>|</b>ABOUT US<b>|</b>CONTACT<b>|</b>SCHEDULE</nav>
<p class="copyright abs">Copyright © 2016 brinewardsea.com. All rights reserved.</p>

</body>
</html>
```